Business card for massage therapy company called Brook Fern Wellness

Need business card for massage therapy company called Brook Fern Wellness. Would like my logo on the front and the back of the card I have 3 options of logos and you can play with what looks better.

Would like this information displayed on the back of the card:

Marcus Ellery
Licensed Massage Therapist
321-555-0147
brookfern-example.com
brookfern_rest_

```html
<!DOCTYPE html>
<html lang="en">
<head>
<meta charset="UTF-8">
<title>Brook Fern Wellness – Business Card</title>
<link rel="stylesheet" href="https://fonts.googleapis.com/css2?family=Tenor+Sans&family=Lato:wght@400&display=swap">
<style>
  :root {
    --backdrop: #dfc9b8;
    --sage: #727760;
    --clay: #c0956f;
    --paper: #ffffff;
    --ink-soft: #6f7360;
  }
  html, body {
    margin: 0;
    padding: 0;
    width: 1200px;
    height: 1200px;
    overflow: hidden;
    background: var(--backdrop);
  }
  .canvas {
    position: relative;
    width: 1200px;
    height: 1200px;
  }
  .card {
    position: absolute;
    left: 278px;
    width: 674px;
    height: 404px;
    border-radius: 36px;
    overflow: hidden;
  }
  .card--front {
    top: 150px;
    background: var(--sage);
  }
  .card--back {
    top: 620px;
    background: var(--paper);
  }

  /* Front */
  .front-mark {
    position: absolute;
    left: 274px;
    top: 72px;
    width: 144px;
    height: 144px;
    border: 2px solid var(--paper);
    border-radius: 50%;
    box-sizing: border-box;
  }
  .front-name {
    position: absolute;
    left: 0;
    right: 0;
    top: 236px;
    text-align: center;
    font-family: "Tenor Sans", sans-serif;
    font-weight: 400;
    color: var(--paper);
    margin: 0;
    line-height: 1;
  }
  .front-name__main {
    display: block;
    font-size: 48px;
    letter-spacing: 2px;
  }
  .front-name__sub {
    display: block;
    margin-top: 12px;
    font-size: 24px;
    letter-spacing: 6px;
  }

  /* Back */
  .back-mark {
    position: absolute;
    left: 70px;
    top: 104px;
    width: 192px;
    height: 192px;
    border: 2px solid var(--sage);
    border-radius: 50%;
    box-sizing: border-box;
    display: flex;
    align-items: center;
    justify-content: center;
    text-align: center;
  }
  .back-mark__name {
    font-family: "Tenor Sans", sans-serif;
    font-weight: 400;
    color: var(--sage);
    font-size: 20px;
    line-height: 1.25;
    letter-spacing: 2px;
    text-transform: uppercase;
  }
  .divider {
    position: absolute;
    left: 323px;
    top: 78px;
    width: 2px;
    height: 241px;
    background: var(--sage);
  }
  .person {
    position: absolute;
    left: 367px;
    top: 106px;
  }
  .person__name {
    margin: 0;
    font-family: "Tenor Sans", sans-serif;
    font-weight: 400;
    font-size: 31px;
    letter-spacing: 2.5px;
    color: var(--ink-soft);
    line-height: 1;
    text-transform: uppercase;
  }
  .person__title {
    margin: 14px 0 0;
    font-family: "Lato", sans-serif;
    font-size: 16px;
    letter-spacing: 0.3px;
    color: var(--clay);
    text-transform: uppercase;
  }
  .contact-list {
    list-style: none;
    margin: 0;
    padding: 0;
    position: absolute;
    left: 367px;
    top: 207px;
  }
  .contact-list__item {
    display: flex;
    align-items: center;
    height: 29px;
    font-family: "Lato", sans-serif;
    font-size: 17px;
    color: var(--ink-soft);
  }
  .contact-list__icon {
    width: 16px;
    height: 16px;
    margin-right: 9px;
    flex: none;
  }
</style>
</head>
<body>
<main class="canvas">
  <section class="card card--front" aria-label="Card front">
    <div class="front-mark" aria-hidden="true"></div>
    <h1 class="front-name">
      <span class="front-name__main">BROOK FERN</span>
      <span class="front-name__sub">WELLNESS</span>
    </h1>
  </section>

  <section class="card card--back" aria-label="Card back">
    <div class="back-mark">
      <span class="back-mark__name">Brook Fern<br>Wellness</span>
    </div>
    <div class="divider" aria-hidden="true"></div>
    <div class="person">
      <h2 class="person__name">Marcus Ellery</h2>
      <p class="person__title">Licensed Massage Therapist</p>
    </div>
    <ul class="contact-list">
      <li class="contact-list__item">
        <svg class="contact-list__icon" viewBox="0 0 16 16" aria-hidden="true">
          <circle cx="8" cy="8" r="8" fill="var(--sage)"/>
          <path d="M5.2 4.2c.4-.3.9-.2 1.1.2l.6 1.2c.2.4.1.8-.2 1l-.4.3c.4.9 1.1 1.6 2 2l.3-.4c.3-.3.7-.4 1-.2l1.2.6c.4.2.5.7.2 1.1l-.5.6c-.4.4-1 .5-1.5.3C7 10.1 5.6 8.7 4.7 6.8c-.2-.5-.1-1.1.3-1.5z" fill="var(--paper)"/>
        </svg>
        321-555-0147
      </li>
      <li class="contact-list__item">
        <svg class="contact-list__icon" viewBox="0 0 16 16" aria-hidden="true">
          <circle cx="8" cy="8" r="8" fill="var(--sage)"/>
          <circle cx="8" cy="8" r="4.2" fill="none" stroke="var(--paper)" stroke-width="1"/>
          <ellipse cx="8" cy="8" rx="1.8" ry="4.2" fill="none" stroke="var(--paper)" stroke-width="1"/>
          <line x1="3.8" y1="8" x2="12.2" y2="8" stroke="var(--paper)" stroke-width="1"/>
        </svg>
        brookfern-example.com
      </li>
      <li class="contact-list__item">
        <svg class="contact-list__icon" viewBox="0 0 16 16" aria-hidden="true">
          <circle cx="8" cy="8" r="8" fill="var(--sage)"/>
          <rect x="4.3" y="5.2" width="7.4" height="5.6" rx="0.8" fill="none" stroke="var(--paper)" stroke-width="1"/>
          <path d="M4.6 5.6 8 8.3l3.4-2.7" fill="none" stroke="var(--paper)" stroke-width="1"/>
        </svg>
        brookfern_rest_
      </li>
    </ul>
  </section>
</main>
</body>
</html>
```